Coffee and fruit juice

We are a malaysian restaurant that also serves aussie coffee and breakfast from 7am to 11am. After 11am we serve malaysian food but we also have a salad and sandwhich bar for people to choose from. We need a poster to hang outside our door to let people know that we are now also serving aussie coffee and breakfast as well as our usual malaysian cuisine.

Target Market(s)

Office location

Industry/Entity Type

Restaurant

Font styles to use
Decorative
Script

Requirements
Must have
• images and word
Nice to have
• something bold to attract people's attention

```html
<!DOCTYPE html>
<html lang="en">
<head>
<meta charset="utf-8">
<title>Aussie Coffee and Breakfast Poster</title>
<link rel="stylesheet" href="https://fonts.googleapis.com/css2?family=Chewy&family=Oranienbaum&display=swap">
<style>
  :root {
    --backdrop: #ebebeb;
    --poster-dark: #16110d;
    --poster-mid: #2a1d14;
    --table-light: #6b4526;
    --headline-brown: #5b3a22;
    --headline-outline: #f4e8d6;
    --hours-red: #d8232a;
    --hours-outline: #fbeee4;
    --body-cream: #f3ead9;
    --accent-orange: #c9712b;
    --accent-green: #1f9a3d;
    --accent-red: #d21f26;
  }
  html, body {
    margin: 0;
    padding: 0;
    width: 923px;
    height: 1200px;
    overflow: hidden;
    background: var(--backdrop);
  }
  .poster {
    position: absolute;
    left: 33px;
    top: 0;
    width: 857px;
    height: 1200px;
    display: block;
  }
  .headline {
    font-family: "Chewy", "Comic Sans MS", cursive;
    fill: var(--headline-brown);
    stroke: var(--headline-outline);
    stroke-width: 4px;
    stroke-linejoin: round;
    paint-order: stroke fill;
  }
  .hours {
    font-family: "Chewy", "Comic Sans MS", cursive;
    fill: var(--hours-red);
    stroke: var(--hours-outline);
    stroke-width: 3px;
    stroke-linejoin: round;
    paint-order: stroke fill;
  }
  .menu-note {
    font-family: "Oranienbaum", Georgia, serif;
    font-size: 36px;
    fill: var(--body-cream);
  }
  .menu-note .malaysian { fill: var(--accent-orange); }
  .menu-note .salad { fill: var(--accent-green); }
  .menu-note .sandwich { fill: var(--accent-red); }
</style>
</head>
<body>
<svg class="poster" viewBox="0 0 657 920" preserveAspectRatio="none" xmlns="http://www.w3.org/2000/svg">
  <defs>
    <linearGradient id="poster-bg" x1="0" y1="0" x2="0" y2="1">
      <stop offset="0" stop-color="var(--poster-mid)"/>
      <stop offset="0.42" stop-color="var(--poster-dark)"/>
      <stop offset="0.6" stop-color="#3a2616"/>
      <stop offset="0.8" stop-color="#2b1c11"/>
      <stop offset="1" stop-color="#1b130d"/>
    </linearGradient>
    <radialGradient id="table-glow" cx="0.5" cy="0.6" r="0.6">
      <stop offset="0" stop-color="var(--table-light)"/>
      <stop offset="1" stop-color="#3a2616" stop-opacity="0"/>
    </radialGradient>
    <radialGradient id="cup-tones" cx="0.5" cy="0.45" r="0.5">
      <stop offset="0" stop-color="#4a3020"/>
      <stop offset="0.55" stop-color="#120c09"/>
      <stop offset="1" stop-color="#5a3a20" stop-opacity="0"/>
    </radialGradient>
  </defs>

  <rect class="poster-background" width="657" height="920" fill="url(#poster-bg)"/>
  <ellipse class="table-light" cx="328" cy="560" rx="380" ry="200" fill="url(#table-glow)"/>

  <text class="headline" x="50" y="84" font-size="64" textLength="175" lengthAdjust="spacingAndGlyphs">AUSSIE</text>
  <text class="headline" x="58" y="183" font-size="110" textLength="270" lengthAdjust="spacingAndGlyphs">COFFEE</text>
  <text class="headline" x="360" y="181" font-size="64" textLength="96" lengthAdjust="spacingAndGlyphs">AND</text>
  <text class="headline" x="48" y="281" font-size="107" textLength="424" lengthAdjust="spacingAndGlyphs">BREAKFAST</text>

  <text class="hours" x="460" y="351" font-size="43" textLength="84" lengthAdjust="spacingAndGlyphs">From</text>
  <text class="hours" x="383" y="406" font-size="57" textLength="233" lengthAdjust="spacingAndGlyphs">7aM to 11aM</text>

  <ellipse class="coffee-photo" role="img" aria-label="Photo of a black cup of coffee with butterfly latte art on a saucer, on a wooden table" cx="322" cy="565" rx="150" ry="140" fill="url(#cup-tones)"/>

  <text class="menu-note" x="52" y="777" textLength="561" lengthAdjust="spacingAndGlyphs">After 11am we serve <tspan class="malaysian">malaysian food</tspan> but</text>
  <text class="menu-note" x="52" y="829" textLength="548" lengthAdjust="spacingAndGlyphs">we also have a <tspan class="salad">salad</tspan> and <tspan class="sandwich">sandwhich</tspan> bar</text>
  <text class="menu-note" x="52" y="880" textLength="359" lengthAdjust="spacingAndGlyphs">for people to choose from.</text>
</svg>
</body>
</html>
```